Web-site design for company trading in chemicals & lubricants

We need a standard 5 page web-site designed for our company based in Dubai, UAE.
The web-site should highlight our capacity to store material as well as distribute the same. The products we sell are basic chemicals - packed in bags as well as drums. Bags are big bags - 25 kgs each as well as drums - 200 litres each. We want to highlight the fact that we huge stocks of this material & can deliver by sea & road,
Please use this site as a ref - http://www.torvane-chemicals.co.uk/
Besides this, we need a page dedicated to finished products that we are selling for use in the auto industry - lubricants, motor oils,brake-fluids, greases, coolants etc. This are packed in large drums as well as small cans.
It would be nice if the site could immediately also provide a ref. to our location - Dubai or that we are based in the Middle East.
We will provide our company logo for reference

```html
<!DOCTYPE html>
<html lang="en">
<head>
<meta charset="utf-8">
<title>Norvask – Chemicals &amp; Lubricants</title>
<link href="https://fonts.googleapis.com/css2?family=Gelasio:wght@400;700&family=Noto+Sans:wght@400;700&display=swap" rel="stylesheet">
<style>
:root{
  --bg:#eeebe2;
  --olive-hi:#b09a3a;
  --olive:#8a7420;
  --olive-lo:#5f4f12;
  --brown:#3f2414;
  --brown-mid:#6a3d22;
  --brown-hi:#8e5c3c;
  --tan:#e3d6ac;
  --tan-lt:#f4ecd6;
  --text:#5e5a52;
  --ink:#2a1a10;
  --white:#fff;
}
*{box-sizing:border-box;margin:0;padding:0}
html,body{width:1117px;height:1200px;overflow:hidden}
body{background:var(--bg);font-family:"Noto Sans",sans-serif;color:var(--text);position:relative}
.serif{font-family:"Gelasio",serif}
.abs{position:absolute}

.main-nav{left:145px;top:0;width:828px;height:41px;display:flex;background:linear-gradient(var(--olive-hi),var(--olive) 55%,var(--olive-lo));border:1px solid #c9b97a;border-top:0}
.main-nav a{font-family:"Gelasio",serif;color:var(--white);font-size:15px;text-decoration:none;display:flex;align-items:center;justify-content:center;border-right:1px solid #c9b97a;text-shadow:1px 1px 1px #3a2d05}
.main-nav a:last-child{border-right:0}

.brand{left:145px;top:88px;display:flex;align-items:center;gap:10px}
.brand-name{font-family:"Gelasio",serif;font-weight:700;font-size:40px;color:var(--brown-mid);letter-spacing:2px}
.brand-dot{width:30px;height:30px;border-radius:50%;background:var(--olive)}

.phone{left:735px;top:82px;display:flex;align-items:center;gap:6px}
.phone-icon{width:40px;height:40px;background:var(--brown);border-radius:5px;display:flex;align-items:center;justify-content:center}
.phone-num{font-family:"Gelasio",serif;font-weight:700;font-size:31px;color:var(--ink);letter-spacing:1px}

.search{left:735px;top:153px;width:236px;height:19px;background:var(--tan);border-top:2px solid #b8aa80;font-size:10px;padding:2px 4px;color:#444;display:flex;justify-content:space-between;align-items:center}

.banner{left:145px;top:172px;width:828px;height:240px;background:var(--white);padding:2px;box-shadow:0 1px 3px rgba(0,0,0,.3)}
.banner-photo{width:100%;height:100%;background:linear-gradient(90deg,#c0892e 0%,#5a3a24 35%,#8a2c20 60%,#2e2a3c 80%,#c9a22a 100%)}

.band{left:0;top:413px;width:1117px;height:25px;background:var(--brown)}
.pager{right:144px;top:5px;display:flex;gap:3px}
.pager span{width:14px;height:13px;background:var(--olive-hi);border:1px solid #e0cf7a;font-size:9px;font-weight:700;color:var(--brown);display:flex;align-items:center;justify-content:center}

.products{left:145px;top:455px;width:185px;height:213px;background:var(--tan);border:1px solid #c9b780}
.box-head{height:31px;background:linear-gradient(var(--brown-hi),var(--brown-mid) 50%,var(--brown));border-radius:4px 4px 0 0;color:var(--white);font-family:"Gelasio",serif;font-size:19px;text-align:center;line-height:31px;text-shadow:1px 1px 1px #000}
.products ul{list-style:none}
.products li{position:absolute;left:0;width:184px;height:22px;background:var(--olive);color:var(--white);font-family:"Gelasio",serif;font-size:14px;padding-left:32px;line-height:22px;text-shadow:1px 1px 1px #3a2d05}
.products li svg{position:absolute;left:11px;top:6px}

.welcome{left:345px;top:449px;width:628px}
.welcome h1{font-family:"Gelasio",serif;font-weight:400;font-size:25px;color:var(--ink);margin-bottom:17px}
.welcome p{font-size:9.9px;line-height:15px;margin-bottom:15px;letter-spacing:.1px}
.read-more{position:absolute;right:5px;top:196px;font-size:10px;color:#4a4030;text-decoration:underline;letter-spacing:.5px}

.panel{top:689px;width:267px;height:266px;background:linear-gradient(var(--tan-lt),var(--tan));border:1px solid #d5c697;border-top:0}
.panel .box-head{height:30px;line-height:30px;margin:0 -1px;font-size:20px}
.news-item{margin:13px 5px 0;border-bottom:1px dotted #6a5a40;padding-bottom:5px;font-size:10px;line-height:15px;color:var(--ink)}
.news-item:last-child{border-bottom:0}
.news-date{font-weight:700;letter-spacing:1px;color:#333}
.news-more{text-align:right;padding-right:5px;font-weight:700;text-decoration:underline;color:var(--ink)}
.quote{padding:16px 12px 0 12px;font-size:10px;line-height:15px;color:var(--ink)}
.quote p{margin-bottom:15px}
.quote-mark{font-family:"Gelasio",serif;font-size:28px;color:var(--brown-mid);line-height:0}
.client{text-align:right;font-weight:700;text-decoration:underline}
.field{margin:0 14px 6px 16px;height:19px;background:#f2e9cb;border:1px solid #c7b88c;border-top:2px solid #a89b72;font-size:10px;padding:2px 6px;color:#333}
.field.msg{height:83px}
.submit{position:absolute;right:14px;top:226px;width:58px;height:20px;background:linear-gradient(var(--olive-hi),var(--olive-lo));border:2px solid #e9dca6;color:var(--white);font-family:"Gelasio",serif;font-weight:700;font-size:12px;text-align:center;line-height:16px}

.footer{left:0;top:976px;width:1117px;height:224px;background:linear-gradient(var(--brown-hi),var(--brown));border-top:2px solid #5a321a}
.foot-col{position:absolute;top:16px}
.foot-col h3{font-family:"Gelasio",serif;font-weight:700;font-size:15px;color:var(--white);margin-bottom:11px}
.foot-col ul{list-style:none}
.foot-col li{font-size:9.5px;color:#f3e8dc;height:19.9px;display:flex;align-items:center;gap:6px}
.copyright{left:145px;top:1172px;width:828px;height:28px;background:linear-gradient(var(--olive-hi),var(--olive-lo));color:var(--white);font-size:10.5px;font-weight:700;text-align:center;line-height:28px;letter-spacing:.5px;text-shadow:1px 1px 1px #000}
</style>
</head>
<body>

<nav class="main-nav abs">
  <a style="flex:100">HOME</a><a style="flex:120">ABOUT</a><a style="flex:150">PARTNERS</a><a style="flex:153">LOGISTICS</a><a style="flex:92">SHE</a><a style="flex:116">REACh</a><a style="flex:110">NEWS</a><a style="flex:159">CONTACT US</a>
</nav>

<div class="brand abs"><span class="brand-name">NORVASK</span><span class="brand-dot"></span></div>

<div class="phone abs">
  <div class="phone-icon"><svg width="22" height="26" viewBox="0 0 22 26"><path d="M5 1c-3 1-4 4-3 8 2 7 6 13 12 16 3 1 5 0 6-2l-4-5-3 2c-3-2-5-6-6-9l3-2z" fill="#fff"/></svg></div>
  <span class="phone-num">123 456 789</span>
</div>

<div class="search abs"><span>Search...</span><svg width="20" height="12" viewBox="0 0 20 12"><circle cx="6" cy="5.5" r="4.5" fill="none" stroke="#111" stroke-width="2"/><line x1="9.5" y1="8" x2="18" y2="11" stroke="#111" stroke-width="2.5"/></svg></div>

<div class="banner abs"><div class="banner-photo" role="img" aria-label="Worker in protective visor connecting a hose to a chemical tank and pipework"></div></div>

<div class="band abs"><div class="pager abs"><span>1</span><span>2</span><span>3</span><span>4</span><span>5</span></div></div>

<aside class="products abs">
  <div class="box-head">Our Products</div>
  <ul>
    <li style="top:43px"><svg width="12" height="10"><path d="M0 0l5 5-5 5M6 0l5 5-5 5" stroke="#fff" stroke-width="2" fill="none"/></svg>Lubricants</li>
    <li style="top:76px"><svg width="12" height="10"><path d="M0 0l5 5-5 5M6 0l5 5-5 5" stroke="#fff" stroke-width="2" fill="none"/></svg>Motor oils</li>
    <li style="top:110px"><svg width="12" height="10"><path d="M0 0l5 5-5 5M6 0l5 5-5 5" stroke="#fff" stroke-width="2" fill="none"/></svg>Brake-fluids</li>
    <li style="top:143px"><svg width="12" height="10"><path d="M0 0l5 5-5 5M6 0l5 5-5 5" stroke="#fff" stroke-width="2" fill="none"/></svg>Greases</li>
    <li style="top:176px"><svg width="12" height="10"><path d="M0 0l5 5-5 5M6 0l5 5-5 5" stroke="#fff" stroke-width="2" fill="none"/></svg>Coolants</li>
  </ul>
</aside>

<section class="welcome abs">
  <h1>Welcome To Our Company</h1>
  <p>Lorem Ipsum is simply dummy text of the printing and typesetting industry. Lorem Ipsum has been the industry's standard dummy text ever since the 1500s, when an unknown printer took a galley of type and scrambled it to make a type specimen book. It has survived not only five centuries, but also the leap into electronic typesetting, remaining essentially unchanged. It was popularised in the 1960s with the release of Letraset sheets containing Lorem Ipsum passages, and more recently.</p>
  <p>It has survived not only five centuries, but also the leap into electronic typesetting, remaining essentially unchanged. It was popularised in the 1960s with the release of Letraset sheets containing Lorem Ipsum passages, and more recently.It has survived not only five centuries, but also the leap into electronic typesetting, remaining essentially unchanged. It was popularised in the 1960s.</p>
  <span class="read-more">READ MORE</span>
</section>

<section class="panel abs" style="left:145px">
  <div class="box-head">Recent News</div>
  <div class="news-item"><div class="news-date">06/10/2011</div>Lorem Ipsum is simply dummy text of the printing and typesetting industry<div class="news-more">Read more</div></div>
  <div class="news-item"><div class="news-date">06/10/2011</div>Lorem Ipsum is simply dummy text of the printing and typesetting industry<div class="news-more">Read more</div></div>
  <div class="news-item"><div class="news-date">06/10/2011</div>Lorem Ipsum is simply dummy text of the printing and typesetting industry<div class="news-more">Read more</div></div>
</section>

<section class="panel abs" style="left:426px">
  <div class="box-head">Testimonials</div>
  <div class="quote">
    <p><span class="quote-mark">&ldquo;</span> Lorem Ipsum is simply dummy text of the printing and typesetting industry. Lorem Ipsum has been the industry's standard dummy text ever since the 1500s, when an unknown printer took a galley of type and scrambled.</p>
    <p>It to make a type specimen book. It has survived not only five centuries, but also the leap into electronic typesetting, remaining essentially unchanged typesetting, remaining essentially unchanged.</p>
    <div class="client">Happy Client <span class="quote-mark" style="text-decoration:none">&rdquo;</span></div>
  </div>
</section>

<section class="panel abs" style="left:706px">
  <div class="box-head">Contact Us</div>
  <div style="height:20px"></div>
  <div class="field">Name:</div>
  <div class="field">Phone:</div>
  <div class="field">Email:</div>
  <div class="field msg">Message:</div>
  <div class="submit">Submit</div>
</section>

<footer class="footer abs">
  <div class="foot-col" style="left:147px"><h3>HOME</h3><ul><li>➜ Simply Dummy</li><li>➜ Simply Dummy</li><li>➜ Simply Dummy</li><li>➜ Simply Dummy</li><li>➜ Simply Dummy</li><li>➜ Simply Dummy</li><li>➜ Simply Dummy</li></ul></div>
  <div class="foot-col" style="left:327px"><h3>ABOUT</h3><ul><li>➜ Simply Dummy</li><li>➜ Simply Dummy</li><li>➜ Simply Dummy</li><li>➜ Simply Dummy</li><li>➜ Simply Dummy</li><li>➜ Simply Dummy</li><li>➜ Simply Dummy</li></ul></div>
  <div class="foot-col" style="left:517px"><h3>PARTNERS</h3><ul><li>➜ Simply Dummy</li><li>➜ Simply Dummy</li><li>➜ Simply Dummy</li><li>➜ Simply Dummy</li><li>➜ Simply Dummy</li><li>➜ Simply Dummy</li><li>➜ Simply Dummy</li></ul></div>
  <div class="foot-col" style="left:713px"><h3>LOGISTICS</h3><ul><li>➜ Simply Dummy</li><li>➜ Simply Dummy</li><li>➜ Simply Dummy</li><li>➜ Simply Dummy</li><li>➜ Simply Dummy</li><li>➜ Simply Dummy</li><li>➜ Simply Dummy</li></ul></div>
  <div class="foot-col" style="left:885px"><h3>REACh</h3><ul><li>➜ Simply Dummy</li><li>➜ Simply Dummy</li><li>➜ Simply Dummy</li><li>➜ Simply Dummy</li><li>➜ Simply Dummy</li><li>➜ Simply Dummy</li><li>➜ Simply Dummy</li></ul></div>
</footer>
<div class="copyright abs">Copyright © 2011 Chemical &amp; Lubricants all rights reserved</div>

</body>
</html>
```